Coral Ridge Networks Ltd

I need a website that is an informational only. We are a construction business building telecommunications sites. Seeing how our company is Coral Ridge the color blue might want to be incorporated in the color scheme.
I can provide more picture of towers and wireless communications if needed.
current website www.coralridgenet.ca

Industry/Entity Type

Wireless Telecommunications, Construction

Coding

Coded - Design and coding required

Number of Pages Required

2 page

Font styles to use
Sans Serif

Colors

Designer to choose colors to be used in the design.

```html
<!DOCTYPE html>
<html lang="en">
<head>
<meta charset="utf-8">
<title>Coral Ridge Networks Ltd</title>
<link href="https://fonts.googleapis.com/css2?family=Montserrat:wght@400;500;600;700&family=Open+Sans:wght@400;600&display=swap" rel="stylesheet">
<style>
:root{
  --orange:#f26a21;
  --ink:#1f1f1f;
  --text:#555;
  --muted:#8a8a8a;
  --light:#f3f4f6;
  --white:#ffffff;
  --line:#e3e3e3;
  --sky-top:#4d7fae;
  --sky-mid:#a9c3dc;
  --snow:#eef3f8;
}
*{box-sizing:border-box;margin:0;padding:0}
html,body{width:1200px;height:2848px;overflow:hidden}
body{background:var(--white);font-family:"Open Sans",Arial,sans-serif;color:var(--text);position:relative}
h1,h2,h3,.brand,.nav a,.btn{font-family:"Montserrat",Arial,sans-serif}

/* hero */
.hero{position:relative;height:600px;overflow:hidden}
.hero-photo{position:absolute;inset:0;background:linear-gradient(180deg,var(--sky-top) 0%,#7ea3c8 30%,var(--sky-mid) 55%,var(--snow) 78%,#dfe7f0 100%)}
.topbar{position:absolute;top:0;left:0;right:0;height:70px;display:flex;align-items:center;justify-content:space-between;padding:0 40px;z-index:2}
.brand{display:flex;align-items:center;gap:10px;color:var(--white);font-weight:600;font-size:16px}
.brand-dot{width:14px;height:14px;border-radius:50%;background:var(--white)}
.nav{display:flex;gap:22px}
.nav a{color:var(--white);text-decoration:none;font-size:10px;letter-spacing:1px;font-weight:600}
.nav a.active{border-bottom:2px solid var(--orange);padding-bottom:3px}
.hero-title{position:absolute;top:225px;left:0;right:0;text-align:center;color:var(--white);font-weight:500;font-size:38px;line-height:48px;letter-spacing:2px;text-transform:uppercase}
.hero-arrow{position:absolute;top:285px;width:24px;height:24px}
.hero-arrow.left{left:18px}.hero-arrow.right{right:18px}
.dots{position:absolute;bottom:58px;left:0;right:0;display:flex;justify-content:center;gap:8px}
.dots span{width:7px;height:7px;border-radius:50%;background:rgba(255,255,255,.6)}
.dots span.on{background:var(--white)}

/* services */
.services{height:260px;background:var(--light);display:flex;justify-content:center;gap:60px;padding-top:60px}
.service{width:280px;text-align:center}
.service svg{width:30px;height:30px}
.service h3{color:var(--ink);font-size:15px;font-weight:600;margin:8px 0 10px}
.service p{font-size:10.5px;line-height:16px}

/* about */
.about{height:290px;text-align:center;padding-top:60px}
.section-title{color:var(--ink);font-size:22px;font-weight:600}
.about .rule{width:40px;height:2px;background:var(--orange);margin:14px auto 26px}
.about p{width:860px;margin:0 auto 8px;font-size:10.5px;line-height:16px}

/* safety */
.safety{height:430px;position:relative}
.safety-copy{position:absolute;left:240px;top:30px;width:200px}
.safety-copy h2{font-size:34px;color:var(--ink);font-weight:500;margin-bottom:22px}
.safety-copy p{font-size:10.5px;line-height:16px;margin-bottom:12px}
.safety-copy ol{font-size:10.5px;line-height:16px;padding-left:16px}
.safety-photo{position:absolute;left:550px;top:10px;width:400px;height:410px;background:linear-gradient(180deg,#2f78c4 0%,#5b98d6 55%,#8fb8e2 100%)}

/* projects */
.projects{height:1020px;position:relative;text-align:center;padding-top:100px}
.projects .lead{font-size:11px;margin-top:10px}
.project-row{position:absolute;top:220px;left:8px;right:8px;display:flex;gap:8px;height:400px}
.project-row div{flex:1}
.p1{background:linear-gradient(180deg,#c9c2b5 0%,#8a7a66 55%,#5f5246 100%)}
.p2{background:linear-gradient(180deg,#6f8fa8 0%,#3f6f9f 45%,#c9d2d8 100%)}
.p3{background:linear-gradient(180deg,#f3f1ee 0%,#e6e0da 60%,#d9cfc6 100%)}

/* cta */
.cta{position:absolute;top:2400px;left:0;right:0;height:200px;background:var(--orange);display:flex;align-items:center;justify-content:space-between;padding:0 240px}
.cta h2{color:var(--white);font-size:22px;font-weight:600}
.cta p{color:var(--white);font-size:11px;margin-top:6px}
.btn{border:1.5px solid var(--white);color:var(--white);font-size:10px;font-weight:600;letter-spacing:1px;padding:9px 18px}

/* footer */
.footer{position:absolute;top:2600px;left:0;right:0;height:248px;background:var(--white)}
.footer-cols{display:flex;gap:120px;padding:40px 0 0 240px}
.footer-col{width:180px;font-size:10px;line-height:16px}
.footer-col h4{font-family:"Montserrat",Arial,sans-serif;color:var(--ink);font-size:10px;letter-spacing:1px;margin-bottom:8px}
.footer-col a{display:block;color:var(--orange);text-decoration:none}
.copyright{position:absolute;bottom:22px;left:0;right:0;text-align:center;font-size:9px;color:var(--muted);border-top:1px solid var(--line);padding-top:14px;margin:0 240px}
</style>
</head>
<body>

<header class="hero">
  <div class="hero-photo" role="img" aria-label="Photograph of a tall communications mast rising from snowy mountain terrain under a blue sky"></div>
  <div class="topbar">
    <div class="brand"><span class="brand-dot"></span>Coral Ridge</div>
    <nav class="nav">
      <a class="active" href="#">HOME</a><a href="#">ABOUT US</a><a href="#">SAFETY</a><a href="#">PROJECTS</a><a href="#">CONTACT</a>
    </nav>
  </div>
  <h1 class="hero-title">We are committed to a<br>strong safety policy</h1>
  <svg class="hero-arrow left" viewBox="0 0 24 24"><path d="M15 4 7 12l8 8" fill="none" stroke="#fff" stroke-width="2.5"/></svg>
  <svg class="hero-arrow right" viewBox="0 0 24 24"><path d="M9 4l8 8-8 8" fill="none" stroke="#fff" stroke-width="2.5"/></svg>
  <div class="dots"><span class="on"></span><span></span><span></span></div>
</header>

<section class="services">
  <div class="service">
    <svg viewBox="0 0 30 30"><path d="M4 15 15 5l11 10h-3v10h-6v-7h-4v7H7V15z" fill="var(--orange)"/></svg>
    <h3>Rooftop Sites</h3>
    <p>We install and maintain antenna systems on commercial rooftops, working safely at height with full structural review and clean cable routing on every site we build.</p>
  </div>
  <div class="service">
    <svg viewBox="0 0 30 30"><path d="M15 6 9 27M15 6l6 21M11 20h8M12.5 14h5" fill="none" stroke="var(--orange)" stroke-width="2"/><circle cx="15" cy="5" r="2.5" fill="var(--orange)"/></svg>
    <h3>Towers and Monopoles</h3>
    <p>Our crews erect new towers and monopoles from foundation to final climb, delivering steel, antennas and lines that are ready for service on schedule.</p>
  </div>
  <div class="service">
    <svg viewBox="0 0 30 30"><rect x="8" y="4" width="14" height="23" fill="var(--orange)"/><g fill="#fff"><rect x="11" y="8" width="3" height="3"/><rect x="16" y="8" width="3" height="3"/><rect x="11" y="14" width="3" height="3"/><rect x="16" y="14" width="3" height="3"/><rect x="13" y="21" width="4" height="6"/></g></svg>
    <h3>In Building</h3>
    <p>Indoor coverage is planned and built with care, bringing strong wireless signal to offices, malls and venues without disturbing the people inside them.</p>
  </div>
</section>

<section class="about">
  <h2 class="section-title">About Us</h2>
  <div class="rule"></div>
  <p>At Coral Ridge we are a full service telecommunications construction firm serving carriers across the country. We combine skilled field crews with careful planning to deliver sites that are safe, tidy and built to last for many years.</p>
  <p>Our certified, professional team is here to support a wide range of projects to meet your requirements.</p>
  <p>To learn more about how our services can help your business, please contact our office by phone or email today.</p>
</section>

<section class="safety">
  <div class="safety-copy">
    <h2>Safety Policy</h2>
    <p>At Coral Ridge Networks all safety is number one. Coral Ridge is committed to a strong safety policy, protecting our staff and the general public from accidents and harm. All Coral Ridge employees are certified Tower Competent Climber and Rescue. In addition to tower safety, we promote safe work practices on every site, including but not limited to the following:</p>
    <ol>
      <li>Fall protection</li>
      <li>All crews first aid trained</li>
      <li>Site safety meetings</li>
      <li>Lockout and tagout procedures</li>
      <li>Hard hats and safety vests</li>
      <li>Working in harsh winter conditions</li>
      <li>Site specific hazard assessments</li>
    </ol>
  </div>
  <div class="safety-photo" role="img" aria-label="Photograph of a lattice telecommunications tower with antennas and dishes against a blue sky"></div>
</section>

<section class="projects">
  <h2 class="section-title">Our Projects</h2>
  <p class="lead">We have made it our mission to provide reliable projects and services to our customer driven approach.</p>
  <div class="project-row">
    <div class="p1" role="img" aria-label="Photograph of equipment shelters on a building rooftop"></div>
    <div class="p2" role="img" aria-label="Photograph of a blue crane lifting tower sections on site"></div>
    <div class="p3" role="img" aria-label="Image of an in-building coverage floor plan"></div>
  </div>
</section>

<section class="cta">
  <div>
    <h2>Coral Ridge Networks Ltd,</h2>
    <p>We value your business</p>
  </div>
  <span class="btn">CONTACT US</span>
</section>

<footer class="footer">
  <div class="footer-cols">
    <div class="footer-col">
      <h4>ABOUT US</h4>
      <p>Our certified, professional team is here to support a range of services to meet your requirements.</p>
    </div>
    <div class="footer-col">
      <h4>CONTACT INFO</h4>
      <p>Address:<br>1234 Harbour Lane<br>Halifax, NS B3K 2R7<br>Phone: (902) 555-0148<br>Email:<br>info@coralridgenet.ca</p>
    </div>
    <div class="footer-col">
      <h4>QUICK LINKS</h4>
      <a href="#">Home</a><a href="#">Safety</a><a href="#">Projects</a>
    </div>
  </div>
  <p class="copyright">All rights reserved 2019 Coral Ridge Networks Ltd</p>
</footer>

</body>
</html>
```